Business Card Design for Marketing Firm

Looking for business card design for higher end marketing firm. Clean but impressionable/trendy. We are a marketing firm that represents manufacturers in the foodservice equipment and supply industry. Our customers are end users such has hotels, restaurants, country clubs, convention centers and casinos as well as distributors of restaurants supplies and equipment, and manufacturers of foodservice equipment and supplies.
Target Market(s)
Hotels, Restaurants, Supply & Equipment Distributors, Foodservice Manufacturers
Industry/Entity Type
Foodservice/Hospitality
Contact Information for Business Card
Name, Title, Contact Number, Email, Website, Social Media, Address
Requirements
Must have
- Clean & Simple but Serious and Impressionable

```html
<!DOCTYPE html>
<html lang="en">
<head>
<meta charset="utf-8">
<title>Meridian Service Partners – Business Card</title>
<link rel="stylesheet" href="https://fonts.googleapis.com/css2?family=Montserrat:wght@400;600;800&family=Open+Sans:wght@400;600&display=swap">
<style>
  :root {
    --navy: #07077f;
    --white: #ffffff;
    --ink-grey: #55555f;
    --stage: #3a3b3e;
  }
  * { box-sizing: border-box; margin: 0; padding: 0; }
  html, body { width: 1200px; height: 952px; overflow: hidden; }
  body {
    background: var(--stage);
    display: flex;
    flex-direction: column;
    align-items: center;
    justify-content: center;
    gap: 48px;
    font-family: "Open Sans", sans-serif;
  }
  .card {
    width: 640px;
    height: 366px;
    border-radius: 26px;
    position: relative;
    overflow: hidden;
    box-shadow: 0 10px 30px rgba(0,0,0,.35);
  }

  /* Front */
  .card--front { background: var(--white); }
  .brand {
    font-family: "Montserrat", sans-serif;
    font-weight: 600;
    letter-spacing: .12em;
    text-transform: uppercase;
    display: flex;
    align-items: center;
    gap: 12px;
    line-height: 1.15;
  }
  .brand__mark { width: 14px; height: 14px; background: currentColor; flex: none; }
  .card--front .brand {
    position: absolute;
    top: 62px;
    left: 250px;
    color: var(--navy);
    font-size: 22px;
  }
  .person {
    position: absolute;
    top: 186px;
    left: 46px;
    color: var(--navy);
  }
  .person__name {
    font-family: "Montserrat", sans-serif;
    font-size: 22px;
    font-weight: 400;
    letter-spacing: .02em;
  }
  .person__name strong { font-weight: 800; }
  .person__title {
    margin-top: 4px;
    font-size: 16px;
    color: var(--ink-grey);
  }
  .contacts {
    position: absolute;
    top: 186px;
    left: 360px;
    list-style: none;
    display: flex;
    flex-direction: column;
    gap: 9px;
    font-size: 14px;
    color: var(--ink-grey);
  }
  .contacts li { display: flex; align-items: center; gap: 10px; }
  .contacts svg { width: 20px; height: 20px; flex: none; }
  .address-band {
    position: absolute;
    left: 0; right: 0; bottom: 40px;
    height: 30px;
    background: var(--navy);
    color: var(--white);
    font-size: 14px;
    letter-spacing: .04em;
    display: flex;
    align-items: center;
    padding-left: 46px;
  }

  /* Back */
  .card--back {
    background: var(--navy);
    display: flex;
    align-items: center;
    justify-content: center;
  }
  .card--back .brand { color: var(--white); font-size: 30px; }
</style>
</head>
<body>
  <section class="card card--front" aria-label="Business card front">
    <div class="brand"><span class="brand__mark"></span><span>Meridian<br>Service Partners</span></div>

    <div class="person">
      <p class="person__name">DANIEL R. <strong>WHITMORE</strong></p>
      <p class="person__title">Managing Director</p>
    </div>

    <ul class="contacts">
      <li>
        <svg viewBox="0 0 20 20" aria-hidden="true"><rect width="20" height="20" rx="4" fill="#07077f"/><path d="M6.5 4.5l2 .3.8 2.5-1.3 1a7 7 0 0 0 3.7 3.7l1-1.3 2.5.8.3 2c-.2 1-1 1.5-2 1.5A10 10 0 0 1 5 6.5c0-1 .5-1.8 1.5-2z" fill="#fff"/></svg>
        <span>+00 987 654 32</span>
      </li>
      <li>
        <svg viewBox="0 0 20 20" aria-hidden="true"><rect width="20" height="20" rx="4" fill="#07077f"/><rect x="4" y="6" width="12" height="8.5" rx="1" fill="none" stroke="#fff" stroke-width="1.5"/><path d="M4.5 6.5l5.5 4.3 5.5-4.3" fill="none" stroke="#fff" stroke-width="1.5"/></svg>
        <span>hello@meridianpartners.com</span>
      </li>
      <li>
        <svg viewBox="0 0 20 20" aria-hidden="true"><rect width="20" height="20" rx="4" fill="#07077f"/><path d="M6 5l8 5-3.4.8 2 3.6-1.5.8-2-3.6L6.5 14z" fill="#fff"/></svg>
        <span>www.meridianpartners.com</span>
      </li>
    </ul>

    <div class="address-band">2170 Harbor Crest Avenue Baltimore, MD 21230</div>
  </section>

  <section class="card card--back" aria-label="Business card back">
    <div class="brand"><span class="brand__mark"></span><span>Meridian<br>Service Partners</span></div>
  </section>
</body>
</html>
```